Banner Ad for Pilot Life Insurance

Aviator Coverage Hub (www.vorntaplan.example). We sell life insurance products to pilots in the United States market. Life Insurance is a highly regulated business so the promises or claims made in advertising is required to be accurate. This is a banner ad for the site skyrolbo.example. It is going in the section Fast Notes.

• 600w x 300h
• 200 kb maximum file size.
• 72dpi, GIF or JPG format.
• Animation is acceptable (15 second maximum).
• Audio can NOT be used.
• Expandable ads are not accepted.
• Flash is not recommended unless the URL click-through is embedded.
• JavaScript is not accepted.

Link to other stuff we have done:
https://www.filebarnex.example/sh/qz7mtrwbnhe2kd4/pLX3rrBe_k

Target Market(s)

Audience is 95% male 40 to 65 year of age in the United States - all are pilots most as their profession.

Industry/Entity Type

Life Insurance

Requirements
Must have
• Banner advertising is not something that has been effective for us in the past. Our best advertising efforts today have been in newsletters with embeded text ads and email industry information newsletters. So it needs something to get attention or call to action.

```html
<!DOCTYPE html>
<html lang="en">
<head>
<meta charset="utf-8">
<title>Life Insurance for Pilots by Pilots – Aviator Coverage Hub</title>
<link rel="stylesheet" href="https://fonts.googleapis.com/css2?family=Arimo:wght@400;700&display=swap">
<style>
  :root {
    --navy: #0b1f5c;
    --navy-deep: #06133d;
    --wave: #16327e;
    --white: #ffffff;
    --button-top: #3f6fc4;
    --button-bottom: #0f2a74;
  }
  * { margin: 0; padding: 0; box-sizing: border-box; }
  html, body { width: 1200px; height: 600px; overflow: hidden; background: var(--white); }
  .banner {
    position: relative;
    width: 1200px;
    height: 600px;
    overflow: hidden;
    font-family: "Arimo", Arial, sans-serif;
    color: var(--navy);
  }
  .banner__backdrop, .banner__photo { position: absolute; }
  .banner__backdrop { left: 0; top: 0; }
  .banner__photo { left: 0; top: 30px; }

  .headline { font-family: "Arimo", Arial, sans-serif; font-weight: 700; }
  .headline__lead, .headline__line {
    position: absolute;
    display: block;
    white-space: nowrap;
    line-height: 1;
  }
  .headline__lead {
    left: 464px;
    top: 16px;
    font-size: 52px;
    color: var(--white);
    text-shadow: 0 0 8px rgba(6, 19, 61, 0.7);
  }
  .headline__line {
    font-size: 100px;
    letter-spacing: -2px;
    color: var(--navy);
    text-shadow: 0 0 6px var(--white), 0 0 14px var(--white);
  }
  .headline__line--first { left: 436px; top: 80px; }
  .headline__line--second { left: 534px; top: 166px; }
  .headline__small { font-size: 50px; letter-spacing: 0; margin-right: 8px; }

  .brand {
    position: absolute;
    left: 914px;
    top: 70px;
    display: flex;
    align-items: center;
    gap: 16px;
  }
  .brand__name {
    font-weight: 700;
    font-size: 16px;
    line-height: 1.3;
    letter-spacing: 4px;
    text-transform: uppercase;
    color: var(--navy);
    width: 150px;
  }
  .brand__mark {
    width: 64px; height: 64px; border-radius: 50%;
    background: var(--navy);
  }

  .benefits {
    position: absolute;
    left: 724px;
    top: 262px;
    width: 472px;
    list-style: none;
    font-weight: 700;
    font-size: 19px;
    line-height: 22px;
    color: var(--navy);
  }
  .benefits__item { position: relative; padding-left: 22px; margin-bottom: 2px; white-space: nowrap; }
  .benefits__item::before {
    content: "";
    position: absolute;
    left: 3px; top: 6px;
    width: 9px; height: 9px;
    background: var(--navy);
    transform: rotate(45deg);
  }

  .cta {
    position: absolute;
    left: 796px;
    top: 500px;
    width: 244px;
    height: 54px;
    border-radius: 27px;
    background: linear-gradient(to bottom, var(--button-top), var(--button-bottom));
    box-shadow: 0 3px 8px rgba(6, 19, 61, 0.55), inset 0 2px 2px rgba(255,255,255,0.35);
    color: var(--white);
    font-weight: 700;
    font-size: 24px;
    letter-spacing: 1px;
    text-decoration: none;
    display: flex;
    align-items: center;
    justify-content: center;
  }

  .contact {
    position: absolute;
    left: 540px;
    top: 566px;
    display: flex;
    align-items: center;
    gap: 40px;
    font-weight: 700;
    font-size: 22px;
    line-height: 26px;
    color: var(--navy);
  }
  .contact__divider {
    width: 10px; height: 10px;
    background: var(--navy);
    transform: rotate(45deg);
  }
</style>
</head>
<body>
<div class="banner">
  <svg class="banner__backdrop" width="1200" height="600" viewBox="0 0 1200 600" aria-hidden="true">
    <defs>
      <linearGradient id="sky" x1="1" y1="0" x2="0" y2="1">
        <stop offset="0" stop-color="#f4f8fd"/>
        <stop offset="0.45" stop-color="#c4d8f1"/>
        <stop offset="0.8" stop-color="#6f97d2"/>
        <stop offset="1" stop-color="#2a58a8"/>
      </linearGradient>
      <radialGradient id="glow" cx="0.35" cy="0.45" r="0.45">
        <stop offset="0" stop-color="#ffffff" stop-opacity="0.85"/>
        <stop offset="1" stop-color="#ffffff" stop-opacity="0"/>
      </radialGradient>
    </defs>
    <rect width="1200" height="600" fill="url(#sky)"/>
    <rect width="1200" height="600" fill="url(#glow)"/>
    <path d="M0 0 H560 C470 20 400 70 330 110 C240 160 150 160 80 200 C40 225 15 250 0 270 Z" fill="var(--wave)"/>
    <path d="M0 600 V470 C80 500 160 560 260 600 Z" fill="#1c4595" opacity="0.7"/>
  </svg>

  <svg class="banner__photo" width="680" height="570" viewBox="0 0 680 570" role="img" aria-label="Silhouette of a parent lifting a young child into the air, with a small twin-engine airplane flying past">
    <defs>
      <radialGradient id="silhouette" cx="0.5" cy="0.5" r="0.55">
        <stop offset="0" stop-color="#06133d"/>
        <stop offset="0.75" stop-color="#0b1f5c" stop-opacity="0.9"/>
        <stop offset="1" stop-color="#0b1f5c" stop-opacity="0"/>
      </radialGradient>
    </defs>
    <ellipse cx="300" cy="300" rx="270" ry="280" fill="url(#silhouette)"/>
  </svg>

  <h1 class="headline">
    <span class="headline__lead">LIFE insurance</span>
    <span class="headline__line headline__line--first"><span class="headline__small">for</span>PILOTS</span>
    <span class="headline__line headline__line--second"><span class="headline__small">by</span>PILOTS</span>
  </h1>

  <div class="brand">
    <span class="brand__name">Aviator Coverage Hub</span>
    <span class="brand__mark"></span>
  </div>

  <ul class="benefits">
    <li class="benefits__item">Full coverage life insurance with no<br>aviation exclusions.</li>
    <li class="benefits__item">Premium rates unavailable through other<br>agencies and associations.</li>
    <li class="benefits__item">Accurate quoting based on your aviation<br>activity and/or medical history.</li>
    <li class="benefits__item">Our application process is quick and easy.</li>
    <li class="benefits__item">We want you to be completely satisfied.</li>
  </ul>

  <a class="cta" href="#">LEARN MORE</a>

  <div class="contact">
    <span class="contact__phone">CALL (800) 555-0147</span>
    <span class="contact__divider"></span>
    <span class="contact__web">www.vorntaplan.example</span>
  </div>
</div>
</body>
</html>
```